Business Card for a Creative Technology based HR services company

Our company name is Lumo8, and we build large communities of HR (human resource) and finance personnels through our mobile platform, and we conduct lots of on-line and off-line activities to get everyone constantly connected. Behind all these, we will also provide on-site HR and finance contractors to our clients, plus a host of other HR-related services. No process in our company takes more than 5-steps.
Our company slogan: Touching Your Future
Target Market(s)
All human resource (HR) and finance personnels, from new entrants to highly experienced senior professionals.
Industry/Entity Type
Finance
Colors
Designer to choose colors to be used in the design.

```html
<!DOCTYPE html>
<html lang="en">
<head>
<meta charset="utf-8">
<title>Lumo8 Business Card</title>
<link rel="stylesheet" href="https://fonts.googleapis.com/css2?family=Exo+2:wght@400;500;600;800&display=swap">
<style>
  :root {
    --navy: #0f2c57;
    --navy-soft: #1d3f72;
    --red: #e3202a;
    --ink: #2b2b2b;
    --card: #ffffff;
    --backdrop: #e9e9ec;
  }
  * { margin: 0; padding: 0; box-sizing: border-box; }
  html, body {
    width: 1200px;
    height: 901px;
    overflow: hidden;
    background: var(--backdrop);
    font-family: "Exo 2", sans-serif;
  }
  .business-card {
    position: absolute;
    left: 150px;
    top: 193px;
    width: 900px;
    height: 514px;
    background: var(--card);
    border-radius: 44px;
    overflow: hidden;
    box-shadow: 0 10px 30px rgba(0,0,0,0.15);
  }
  .footer-band {
    position: absolute;
    left: 0;
    bottom: 0;
    width: 100%;
    height: 100px;
    background: linear-gradient(100deg, var(--navy) 0%, var(--navy-soft) 100%);
  }
  .brand {
    position: absolute;
    left: 62px;
    top: 52px;
    display: flex;
    align-items: center;
    gap: 12px;
  }
  .brand-name {
    font-weight: 800;
    font-size: 64px;
    color: var(--navy);
    letter-spacing: -1px;
    line-height: 1;
  }
  .brand-dot {
    width: 22px; height: 22px;
    border-radius: 50%;
    background: var(--red);
  }
  .contact-block {
    position: absolute;
    left: 545px;
    top: 100px;
    color: var(--ink);
  }
  .person-name {
    font-weight: 600;
    font-size: 25px;
    color: var(--red);
    letter-spacing: 1px;
    text-transform: uppercase;
    line-height: 1.1;
  }
  .person-role {
    font-weight: 500;
    font-size: 21px;
    line-height: 1.2;
  }
  .address {
    margin-top: 28px;
    font-weight: 500;
    font-size: 21px;
    line-height: 1.25;
  }
  .contact-list {
    list-style: none;
    margin-top: 18px;
    margin-left: -34px;
  }
  .contact-list li {
    display: flex;
    align-items: center;
    gap: 12px;
    font-size: 18px;
    font-weight: 500;
    height: 26px;
  }
  .contact-list svg { width: 18px; height: 18px; flex: none; }
</style>
</head>
<body>
  <div class="business-card">
    <div class="footer-band" role="img" aria-label="Decorative navy band along the lower edge of the card"></div>

    <div class="brand">
      <span class="brand-name">Lumo8</span>
      <span class="brand-dot"></span>
    </div>

    <div class="contact-block">
      <p class="person-name">Daniel Whitmore</p>
      <p class="person-role">Managing Director</p>
      <p class="address">047,12th floor,Harbor<br>Point Road KLM</p>

      <ul class="contact-list">
        <li>
          <svg viewBox="0 0 24 24"><path fill="var(--red)" d="M6.6 10.8a15 15 0 0 0 6.6 6.6l2.2-2.2c.3-.3.7-.4 1-.2 1.1.4 2.3.6 3.6.6.6 0 1 .4 1 1V20c0 .6-.4 1-1 1A17 17 0 0 1 3 4c0-.6.4-1 1-1h3.5c.6 0 1 .4 1 1 0 1.3.2 2.5.6 3.6.1.3 0 .7-.2 1z"/></svg>
          <span>014 628 3057</span>
        </li>
        <li>
          <svg viewBox="0 0 24 24"><rect x="6" y="2" width="12" height="20" rx="2" fill="none" stroke="var(--red)" stroke-width="2"/><circle cx="12" cy="18" r="1.3" fill="var(--red)"/></svg>
          <span>014 628 3057</span>
        </li>
        <li>
          <svg viewBox="0 0 24 24"><rect x="3" y="9" width="18" height="10" rx="1.5" fill="var(--red)"/><rect x="7" y="3" width="10" height="6" fill="none" stroke="var(--red)" stroke-width="2"/><rect x="7" y="14" width="10" height="7" fill="#fff" stroke="var(--red)" stroke-width="1.5"/></svg>
          <span>014 628 3057</span>
        </li>
        <li>
          <svg viewBox="0 0 24 24"><rect x="2" y="5" width="20" height="14" rx="1.5" fill="var(--red)"/><path d="M3 6l9 7 9-7" fill="none" stroke="#fff" stroke-width="1.8"/></svg>
          <span>hello@lumo8mail.com</span>
        </li>
        <li>
          <svg viewBox="0 0 24 24"><circle cx="12" cy="12" r="10" fill="var(--red)"/><path d="M2 12h20M12 2c3 3 3 17 0 20M12 2c-3 3-3 17 0 20" fill="none" stroke="#fff" stroke-width="1.4"/></svg>
          <span>www.lumo8site.com</span>
        </li>
      </ul>
    </div>
  </div>
</body>
</html>
```